Dune Air & Plus business card

I need an awesome, double-sided business card designed with our new logo. I would like the one side black with the colored logo, and the back side is all yours. I'd like to see horizontal and vertical layouts. Get creative! Thank you.

Target Market(s)

HVAC, Heating and Cooling in Phoenix, AZ

Industry/Entity Type

HVAC

Contact Information for Business Card

We need our new logo on the card. Tom Harker, (623) 555-0142, tom@trydunesair.com, www.trydunesair.com, ROC 514273

```html
<!DOCTYPE html>
<html lang="en">
<head>
<meta charset="utf-8">
<title>Dune Air &amp; Plus business card</title>
<link rel="stylesheet" href="https://fonts.googleapis.com/css2?family=Barlow:wght@400;500;700&display=swap">
<style>
  :root {
    --page: #e9e7e3;
    --card: #1b1b1c;
    --orange: #e8952f;
    --copper: #b86a35;
    --blue: #3f8fd6;
    --muted: #6e4a30;
  }
  * { box-sizing: border-box; margin: 0; padding: 0; }
  html, body { width: 1200px; height: 1200px; overflow: hidden; background: var(--page); }
  body { position: relative; font-family: "Barlow", sans-serif; }
  .card {
    position: absolute; left: 220px; width: 760px; height: 435px;
    background: var(--card); box-shadow: 0 10px 28px rgba(0,0,0,.25);
  }
  .card-front { top: 150px; }
  .card-back { top: 615px; }
  .brand {
    position: absolute; left: 0; right: 0; text-align: center;
    font-weight: 700; letter-spacing: 2px; text-transform: uppercase;
  }
  .card-front .brand { top: 88px; font-size: 34px; color: var(--orange); }
  .holder {
    position: absolute; top: 176px; left: 0; right: 0; text-align: center;
    font-size: 29px; letter-spacing: 1.5px; color: var(--orange); text-transform: uppercase;
  }
  .holder svg { vertical-align: -3px; margin-right: 8px; }
  .rule-h { position: absolute; top: 276px; left: 54px; width: 652px; height: 2px; background: var(--orange); }
  .rule-v { position: absolute; top: 276px; width: 2px; height: 110px; background: var(--orange); }
  .rule-v.one { left: 260px; }
  .rule-v.two { left: 534px; }
  .contact { position: absolute; font-size: 21px; color: var(--orange); white-space: nowrap; }
  .contact svg { vertical-align: -3px; margin-right: 10px; }
  .phone { left: 50px; top: 300px; }
  .email { left: 276px; top: 300px; }
  .web { left: 276px; top: 336px; }
  .licence { left: 568px; top: 300px; font-size: 22px; }
  .card-back .brand { top: 186px; font-size: 42px; color: var(--copper); }
  .card-back .dot {
    display: inline-block; width: 14px; height: 14px; border-radius: 50%;
    background: var(--copper); margin-right: 12px; vertical-align: 6px;
  }
  .tagline {
    position: absolute; top: 318px; left: 0; right: 0; text-align: center;
    font-size: 13px; color: var(--muted);
  }
</style>
</head>
<body>
  <section class="card card-front" aria-label="Card front">
    <div class="brand">Dune Air &amp; Plus</div>
    <div class="holder">
      <svg width="24" height="24" viewBox="0 0 24 24" aria-hidden="true">
        <circle cx="12" cy="12" r="11" fill="var(--blue)"/>
        <circle cx="12" cy="9.5" r="4" fill="var(--card)"/>
        <path d="M4.8 19.5c1.6-3.2 4.2-4.6 7.2-4.6s5.6 1.4 7.2 4.6" fill="var(--card)"/>
      </svg>Tom Harker
    </div>
    <div class="rule-h"></div>
    <div class="rule-v one"></div>
    <div class="rule-v two"></div>
    <div class="contact phone">
      <svg width="20" height="20" viewBox="0 0 24 24" aria-hidden="true"><path d="M6.6 10.8a15 15 0 0 0 6.6 6.6l2.2-2.2c.3-.3.7-.4 1-.2 1.1.4 2.3.6 3.6.6.6 0 1 .4 1 1V20c0 .6-.4 1-1 1A17 17 0 0 1 3 4c0-.6.4-1 1-1h3.5c.6 0 1 .4 1 1 0 1.3.2 2.5.6 3.6.1.3 0 .7-.2 1z" fill="var(--blue)"/></svg>(623) 555-0142
    </div>
    <div class="contact email">
      <svg width="16" height="16" viewBox="0 0 24 24" aria-hidden="true"><rect x="2" y="5" width="20" height="14" rx="2" fill="none" stroke="var(--blue)" stroke-width="2.4"/><path d="M3 6l9 7 9-7" fill="none" stroke="var(--blue)" stroke-width="2.4"/></svg>tom@trydunesair.com
    </div>
    <div class="contact web">
      <svg width="16" height="16" viewBox="0 0 24 24" aria-hidden="true"><circle cx="12" cy="12" r="10" fill="none" stroke="var(--blue)" stroke-width="2.2"/><ellipse cx="12" cy="12" rx="4.5" ry="10" fill="none" stroke="var(--blue)" stroke-width="2"/><path d="M2 12h20" stroke="var(--blue)" stroke-width="2"/></svg>www.trydunesair.com
    </div>
    <div class="contact licence">ROC 514273</div>
  </section>

  <section class="card card-back" aria-label="Card back">
    <div class="brand"><span class="dot"></span>Dune Air &amp; Plus</div>
    <p class="tagline">HVAC, Heating and Cooling in Phoenix, AZ</p>
  </section>
</body>
</html>
```